Label for high-end indie coffee package

I need a label for high-end indie coffee package.

Coffee comes from Mt. Elgon, Trans-Nzoia County, Kenya. The coffee will be sold in Finland. The package as such will be semi matte black and the label will be printed out as a sticker.

Maximum measurements for the label would around 9 x 9 centimeters. It can be a square / rectangle / circle. I would like it to include influences from coffee origins (Kenya) and also demonstrate the high-end quality of the coffee with the modern twist.

The label should include the following text:

Coffee Name:
Morelu Vintaro AA
Washed & Natural

Origins:
Mt. Elgon, Trans-Nzoia County, Kenya

Growing altitude:
Altitude: 1 800 amsl

Coffee variety:
100 % Arabica

Following fields should be possible to be filled afterwards when the need occurs:
roast date
best before
roasted by

I'll be more than happy to answer any questions!

Finland. High-end customers, design coffee shops.

```html
<!DOCTYPE html>
<html lang="en">
<head>
<meta charset="utf-8">
<title>Morelu Vintaro AA – Coffee Label</title>
<link rel="stylesheet" href="https://fonts.googleapis.com/css2?family=Montserrat:wght@400;700;800&display=swap">
<style>
  :root {
    --backdrop: #6d6e71;
    --paper: #ffffff;
    --ink: #111111;
    --bean-dark: #1c1c1c;
    --bean-mid: #3b3b3b;
    --sketch: #d9d9d9;
  }
  * { box-sizing: border-box; margin: 0; padding: 0; }
  html, body {
    width: 1200px; height: 1200px; overflow: hidden;
    background: var(--backdrop);
    font-family: "Montserrat", Arial, sans-serif;
    color: var(--ink);
  }
  .label {
    position: absolute; left: 96px; top: 96px;
    width: 1008px; height: 1008px;
    background: var(--paper);
    box-shadow: 8px 8px 10px rgba(0,0,0,0.35);
    overflow: hidden;
  }
  .rules { position: absolute; inset: 0; }
  .rules line { stroke: var(--ink); stroke-width: 2.4; }
  .title {
    position: absolute; left: 124px; top: 114px;
    font-weight: 800; font-size: 104px; line-height: 104px;
    letter-spacing: -1px; text-transform: uppercase;
  }
  .process {
    position: absolute; left: 336px; top: 348px; width: 610px;
    font-weight: 700; font-size: 37px; letter-spacing: 0.2em;
    text-align: center; line-height: 60px; text-transform: uppercase;
  }
  .plant-art {
    position: absolute; left: 696px; top: 88px; width: 196px; height: 232px;
    background: radial-gradient(ellipse at 55% 50%, var(--sketch), rgba(255,255,255,0) 70%);
  }
  .field { position: absolute; }
  .field .caption { font-weight: 400; font-size: 24px; line-height: 30px; }
  .field .value { font-weight: 700; font-size: 31px; line-height: 38px; }
  .field.small .value { font-size: 30px; }
  .field.centered { text-align: center; }
  .origins { left: 124px; top: 464px; }
  .variety { left: 124px; top: 580px; }
  .altitude { left: 522px; top: 578px; }
  .roast-date { left: 124px; top: 702px; }
  .best-before { left: 376px; top: 702px; width: 284px; }
  .roasted-by { left: 660px; top: 702px; width: 296px; }
  .roasted-by .value { line-height: 38px; }
  .bean-bed {
    position: absolute; left: 0; top: 828px; width: 1008px; height: 180px;
    background: linear-gradient(180deg, var(--bean-mid), var(--bean-dark));
    border-radius: 40px 40px 0 0 / 30px 30px 0 0;
  }
</style>
</head>
<body>
  <div class="label">
    <svg class="rules" width="1008" height="1008" viewBox="0 0 1008 1008">
      <line x1="32" y1="32" x2="976" y2="32"/>
      <line x1="32" y1="32" x2="32" y2="900"/>
      <line x1="976" y1="32" x2="976" y2="900"/>
      <line x1="336" y1="342" x2="946" y2="342"/>
      <line x1="336" y1="410" x2="946" y2="410"/>
      <line x1="92" y1="448" x2="946" y2="448"/>
      <line x1="92" y1="566" x2="946" y2="566"/>
      <line x1="460" y1="570" x2="460" y2="672"/>
      <line x1="92" y1="682" x2="946" y2="682"/>
      <line x1="376" y1="692" x2="376" y2="860"/>
      <line x1="660" y1="692" x2="660" y2="860"/>
    </svg>

    <h1 class="title">Morelu<br>Vintaro<br>AA</h1>
    <div class="plant-art" role="img" aria-label="Engraved illustration of a coffee plant branch with leaves"></div>
    <p class="process">Washed &amp; Natural</p>

    <div class="field origins">
      <p class="caption">Origins:</p>
      <p class="value">Mt. Elgon, Trans-Nzoia County, Kenya</p>
    </div>
    <div class="field variety">
      <p class="caption">Coffee variety:</p>
      <p class="value">100 % Arabica</p>
    </div>
    <div class="field altitude">
      <p class="caption">Growing altitude:</p>
      <p class="value">Altitude: 1 800 amsl</p>
    </div>
    <div class="field small roast-date">
      <p class="caption">roast date</p>
      <p class="value">00.00.00</p>
    </div>
    <div class="field small centered best-before">
      <p class="caption">best before</p>
      <p class="value">00.00.00</p>
    </div>
    <div class="field small centered roasted-by">
      <p class="caption">roasted by</p>
      <p class="value">Rans-Nzoia<br>County</p>
    </div>

    <div class="bean-bed" role="img" aria-label="Illustrated pile of dark roasted coffee beans along the bottom edge"></div>
  </div>
</body>
</html>
```